Corvane Supplies Business Card

Professional business card that stand out to our potential customers. Front and back with clean modern design

Industry/Entity Type

Oil and gas

Contact Information for Business Card

Name, address, website , office phone and cell number

Requirements
Must have
• Editable files for each employee

```html
<!DOCTYPE html>
<html lang="en">
<head>
<meta charset="UTF-8">
<title>Corvane Supplies Business Card</title>
<link href="https://fonts.googleapis.com/css2?family=Montserrat:wght@700;800&family=Open+Sans:wght@400;600&display=swap" rel="stylesheet">
<style>
  :root {
    --brand-red: #ec2227;
    --brand-blue: #0aaed0;
    --paper: #ffffff;
    --ink: #1b1b1b;
    --backdrop: #3a3836;
  }
  * { box-sizing: border-box; margin: 0; padding: 0; }
  html, body { width: 1200px; height: 900px; overflow: hidden; }
  body {
    background: var(--backdrop);
    font-family: "Open Sans", sans-serif;
    position: relative;
  }
  .card {
    position: absolute;
    left: 250px;
    width: 700px;
    height: 400px;
    border-radius: 26px;
    overflow: hidden;
    box-shadow: 0 10px 24px rgba(0,0,0,0.45);
  }
  .card--front { top: 40px; background: var(--brand-red); }
  .card--back { top: 470px; background: var(--paper); }

  .brand {
    position: absolute;
    display: flex;
    align-items: center;
    gap: 14px;
    font-family: "Montserrat", sans-serif;
    font-weight: 800;
    text-transform: uppercase;
    letter-spacing: 1px;
  }
  .brand__mark { display: block; }
  .card--front .brand {
    left: 0; right: 0; top: 170px;
    justify-content: center;
    color: var(--paper);
    font-size: 44px;
  }
  .card--front .brand__mark { width: 40px; height: 40px; background: var(--paper); }
  .card--back .brand {
    left: 50px; top: 170px;
    color: var(--brand-red);
    font-size: 24px;
  }
  .card--back .brand__mark { width: 24px; height: 24px; background: var(--brand-red); }

  .divider { position: absolute; left: 0; top: 0; }
  .wave { position: absolute; left: 0; top: 0; }

  .contact {
    position: absolute;
    left: 420px;
    top: 34px;
    color: var(--ink);
  }
  .contact__name {
    font-family: "Montserrat", sans-serif;
    font-weight: 800;
    font-size: 24px;
    color: var(--brand-red);
    letter-spacing: 0.5px;
    line-height: 1.1;
  }
  .contact__role { font-size: 15px; margin-bottom: 10px; }
  .contact__address { font-size: 14px; line-height: 1.35; margin-bottom: 10px; }
  .contact__list { list-style: none; }
  .contact__item {
    display: flex;
    align-items: center;
    gap: 9px;
    font-size: 14px;
    line-height: 1;
    margin-bottom: 7px;
  }
  .contact__icon {
    width: 18px; height: 18px;
    background: var(--brand-red);
    display: flex; align-items: center; justify-content: center;
    flex: none;
  }
  .contact__highlight { color: var(--brand-red); }
</style>
</head>
<body>

  <section class="card card--front" aria-label="Card front">
    <div class="brand"><span class="brand__mark"></span>Corvane Supplies</div>
  </section>

  <section class="card card--back" aria-label="Card back">
    <svg class="wave" width="700" height="400" viewBox="0 0 700 400" aria-hidden="true">
      <path d="M0,330 C300,322 470,300 560,240 C610,205 640,200 650,196 C560,280 460,320 0,348 Z" fill="var(--brand-blue)"/>
      <path d="M0,358 C300,348 480,330 570,268 C630,228 665,222 700,220 L700,400 L0,400 Z" fill="var(--brand-red)"/>
    </svg>

    <svg class="divider" width="700" height="400" viewBox="0 0 700 400" aria-hidden="true">
      <line x1="355" y1="60" x2="392" y2="250" stroke="var(--brand-blue)" stroke-width="1.5"/>
      <line x1="372" y1="80" x2="400" y2="215" stroke="var(--brand-red)" stroke-width="1.5"/>
      <line x1="345" y1="110" x2="375" y2="240" stroke="var(--brand-red)" stroke-width="1.5"/>
    </svg>

    <div class="brand"><span class="brand__mark"></span>Corvane Supplies</div>

    <div class="contact">
      <p class="contact__name">DALEN WHITCOMBE</p>
      <p class="contact__role">President</p>
      <p class="contact__address">482 Harlow Ave, Ste<br>210, Midland, TX 79701</p>
      <ul class="contact__list">
        <li class="contact__item">
          <span class="contact__icon"><svg width="12" height="12" viewBox="0 0 12 12"><path d="M2,1 L4.5,1 L5.5,3.5 L4,4.5 C4.7,6 6,7.3 7.5,8 L8.5,6.5 L11,7.5 L11,10 C6,10.5 1.5,6 2,1 Z" fill="#fff"/></svg></span>
          432-555-0147
        </li>
        <li class="contact__item">
          <span class="contact__icon"><svg width="12" height="12" viewBox="0 0 12 12"><rect x="3" y="1" width="6" height="10" rx="1" fill="none" stroke="#fff" stroke-width="1.2"/><circle cx="6" cy="9" r="0.7" fill="#fff"/></svg></span>
          000-000-9999
        </li>
        <li class="contact__item">
          <span class="contact__icon"><svg width="12" height="12" viewBox="0 0 12 12"><rect x="1" y="3" width="10" height="7" fill="none" stroke="#fff" stroke-width="1.2"/><path d="M1,3 L6,7 L11,3" fill="none" stroke="#fff" stroke-width="1.2"/></svg></span>
          info@example-youremail.com
        </li>
        <li class="contact__item">
          <span class="contact__icon"><svg width="12" height="12" viewBox="0 0 12 12"><circle cx="6" cy="6" r="4.5" fill="none" stroke="#fff" stroke-width="1.2"/><path d="M1.5,6 L10.5,6 M6,1.5 C4,4 4,8 6,10.5 M6,1.5 C8,4 8,8 6,10.5" fill="none" stroke="#fff" stroke-width="1"/></svg></span>
          <span>www.<span class="contact__highlight">example-yourwebsite</span>.com</span>
        </li>
      </ul>
    </div>
  </section>

</body>
</html>
```